Varnoth Immigration _Cloud-based, boutique law firm serving clients worldwide in US Immigration Law

I need a website for my new US immigration law firm that will be based in Montreal, QC Canada but serve clients worldwide to achieve their US immigration goals. This will be a boutique firm offering attentive and compassionate service to our corporate and individual clients. I'd like the site to be fresh, modern, sophisticated and easy to read.

I will need a home page, about/bio page, services page, and contact me page with a form so potential clients could email inquiries and also schedule consultations. I would also like a 'Book a Consultation' button on the home page (easily visible).

The longest website page is going to be the 'Services' tab, which I'd like to break down to services for Employers and services Individuals, with further sub-sets of services to each type of client. I envision images with short text that display longer text when hoovering over.

To start, I would have 3 subsets of services for Employers and 5 subsets of services for Individuals. I will need the ability to expand/edit these pages in Wix interface as we grow.

The site will need to be in English and in French.

I like the color blue and the final design should communicate the firm's core values: integrity and compassion. In other words, we do right, no matter what and are understanding to individual circumstances. I'd like the site to convey sophistication and accessibility. I don't like staged stock photos of people. Sites with a lot of stock photos of people feels unauthentic to me.

Logo draft is attached in jpeg. Navy and gold colors.
Example of 4 law firm sites I like below:
- https://www.quellanlawzpt.com/
-https://www.tvbrelaw.com/
-https://kemblinappeals.com/
-https://www.orundalaw.com/

Target Market(s)

Small-medium sized businesses (10-999 employees) in US with foreign workforce; Foreign entrepreneurs wishing to implant in the US

Industry/Entity Type

Law

Coding

Coded - Design and coding required

Font styles to use
Sans Serif

Colors

Designer to choose colors to be used in the design.

Requirements
Must have
• Great Home Page (Grabs attention with eye-catching images/text; Immediately establishes credibility; Provides an overview of services; Encourages visitor to take the next action.)
Nice to have
• Images of Montreal (where firm is based); Images of bridges (symbolizes progress, movement, connections)
Should not have
• Non-authentic photos: staged people at desks or pictures of court buildings.

```html
<!DOCTYPE html>
<html lang="en">
<head>
<meta charset="utf-8">
<title>Varnoth Immigration</title>
<link href="https://fonts.googleapis.com/css2?family=PT+Serif:wght@400;700&family=Poppins:wght@400;500&display=swap" rel="stylesheet">
<style>
:root{
  --navy:#142c3a;
  --navy-deep:#0f2230;
  --gold:#c4962c;
  --sand:#ecd59b;
  --ink:#1d2b36;
  --text:#3d4750;
  --paper:#ffffff;
  --mist:#f1ede7;
}
*{box-sizing:border-box;margin:0;padding:0}
html,body{width:1200px;height:3585px;overflow:hidden}
body{position:relative;font-family:'PT Serif',serif;color:var(--text);background:var(--paper)}
.abs{position:absolute}
a{color:inherit;text-decoration:none}

/* header */
.topbar{left:306px;top:0;width:894px;height:44px;background:var(--navy);clip-path:polygon(0 0,100% 0,100% 100%,24px 100%)}
.topbar .contact{position:absolute;top:0;height:44px;display:flex;align-items:center;gap:12px;color:#fff;font-size:15px}
.ico{width:28px;height:28px;border-radius:50%;border:1.5px solid #fff;display:flex;align-items:center;justify-content:center}
.quote-btn{left:880px;top:0;width:207px;height:44px;background:var(--gold);color:#fff;font-weight:700;font-size:16px;display:flex;align-items:center;justify-content:center}
.brand{display:flex;align-items:center;gap:10px}
.brand .mark{width:44px;height:44px;border-radius:50%;background:#cfc4b3}
.brand .name{font-family:'PT Serif',serif;font-size:17px;letter-spacing:3px;color:#9a8f80;text-transform:uppercase;line-height:1.15}
.nav{left:398px;top:68px;display:flex;gap:24px;font-size:16px;font-weight:700;color:var(--ink);align-items:center}
.nav .sep{color:#888;font-weight:400}
.lang{left:998px;top:64px;display:flex;align-items:center;gap:10px;font-weight:700;color:var(--ink);font-size:16px}
.flag{width:20px;height:20px;border-radius:50%;background:#d8232a;position:relative}
.flag:after{content:"";position:absolute;left:6px;top:0;width:8px;height:20px;background:#fff}

/* hero */
.hero{left:0;top:107px;width:1200px;height:514px;background:linear-gradient(180deg,#0d1822 0%,#1b2c3a 55%,#2a3846 100%)}
.hero-band{left:0;top:575px;width:1200px;height:46px;background:var(--sand);clip-path:polygon(0 100%,100% 0,100% 100%)}
.hero h1{left:0;width:1200px;top:218px;text-align:center;color:#fff;font-size:44px;line-height:50px;font-weight:700;text-transform:uppercase}
.hero-copy{left:0;width:1200px;top:332px;text-align:center;color:#fff;font-size:15px;line-height:24px}
.btn{display:flex;align-items:center;justify-content:center;font-weight:700;font-size:16px;text-transform:uppercase;color:#fff}
.btn-gold{background:var(--gold)}
.btn-navy{background:var(--navy)}

/* about */
.about{left:0;top:621px;width:1200px;height:585px;background:linear-gradient(90deg,#ece6de,#f6f3ef 60%,#f3efe9)}
.about h2{left:112px;top:678px;font-size:36px;line-height:43px;color:var(--navy);text-transform:uppercase}
.about-copy{left:112px;top:777px;width:468px;font-size:15px;line-height:24px;text-align:justify}
.about-copy p+p{margin-top:10px}
.dropcap{float:left;font-size:30px;color:var(--gold);font-weight:700;line-height:30px;margin-right:6px;margin-top:4px}
.frame-a{left:702px;top:680px;width:120px;height:110px;border-top:10px solid var(--gold);border-left:10px solid var(--gold)}
.frame-b{left:752px;top:745px;width:348px;height:368px;border:3px solid var(--gold);border-top:none;border-left:none}
.frame-b:before{content:"";position:absolute;left:0;bottom:0;width:3px;height:20px;background:var(--gold)}
.photo{background:linear-gradient(160deg,#e6e6e6,#cfd2d5)}

/* practice */
.practice{left:0;top:1206px;width:1200px;height:886px;background:var(--navy)}
.section-title{left:0;width:1200px;text-align:center;font-size:36px;font-weight:700;text-transform:uppercase}
.card{width:228px;height:286px;overflow:hidden}
.card .title{position:absolute;left:0;right:0;bottom:36px;text-align:center;color:#fff;font-size:21px;line-height:29px;font-weight:700}
.card .shade{position:absolute;inset:0;background:linear-gradient(180deg,transparent 45%,rgba(10,20,30,.85))}
.card.active{background:linear-gradient(160deg,#d3ab4a,#c4962c)}
.card.active .inner{position:absolute;left:14px;right:14px;top:20px;text-align:center;color:#fff}
.card.active h3{font-size:21px;margin:12px 0 8px}
.card.active p{font-size:14px;line-height:21px}
.outline-btn{left:491px;top:1988px;width:218px;height:47px;border:1.5px solid #fff;color:#fff;font-size:15px}
.practice-band{left:0;top:2047px;width:1200px;height:48px;background:var(--sand);clip-path:polygon(0 0,100% 70%,100% 100%,0 100%)}

/* testimonials */
.testi-card{left:112px;top:2254px;width:976px;height:356px;background:var(--navy)}
.testi-band{left:112px;top:2582px;width:976px;height:28px;background:var(--sand);clip-path:polygon(0 100%,100% 0,100% 100%)}
.quote-box{left:200px;top:2222px;width:122px;height:106px;background:var(--sand);border:4px solid #fff;box-shadow:0 2px 6px rgba(0,0,0,.15);display:flex;align-items:center;justify-content:center}
.testi-copy{left:170px;top:2360px;width:860px;text-align:center;color:#fff;font-size:15px;line-height:24px}
.testi-name{left:0;width:1200px;top:2518px;text-align:center;color:var(--gold);font-size:24px}

/* schedule */
.skyline{left:0;top:2930px;width:1200px;height:228px;background:linear-gradient(180deg,rgba(255,255,255,0),#cfcfcf 70%,#bdbdbd)}
.field{height:60px;border:1.5px solid #9a9a9a;border-radius:4px;background:#fff;font-family:'Poppins',sans-serif;font-size:15px;color:#333;padding:0 24px;display:flex;align-items:center}

/* footer */
.footer{left:0;top:3158px;width:1200px;height:374px;background:var(--navy)}
.footer-nav{left:0;width:1200px;top:3330px;display:flex;justify-content:center;gap:46px;color:#fff;font-size:15px}
.footer-nav .sep{color:#aaa}
.info{top:3390px;display:flex;gap:18px;color:#fff}
.info .badge{width:46px;height:46px;border-radius:50%;background:var(--gold);display:flex;align-items:center;justify-content:center;flex:none}
.info h4{font-size:24px;font-weight:400;margin-bottom:6px}
.info p{font-size:15px;line-height:24px}
.divider{top:3375px;width:1px;height:140px;background:rgba(255,255,255,.25)}
.legal{left:0;top:3532px;width:1200px;height:53px;background:var(--sand);display:flex;align-items:center;justify-content:center;font-family:'Poppins',sans-serif;font-size:14px;color:var(--ink)}
</style>
</head>
<body>

<!-- header -->
<div class="abs brand" style="left:112px;top:36px">
  <span class="mark"></span>
  <span class="name">Varnoth<br>Immigration</span>
</div>
<div class="abs topbar">
  <div class="contact" style="left:85px">
    <span class="ico"><svg width="14" height="14" viewBox="0 0 24 24" fill="#fff"><path d="M6.6 10.8a15 15 0 006.6 6.6l2.2-2.2c.3-.3.7-.4 1-.2 1.1.4 2.3.6 3.6.6.6 0 1 .4 1 1V20c0 .6-.4 1-1 1A17 17 0 013 4c0-.6.4-1 1-1h3.5c.6 0 1 .4 1 1 0 1.3.2 2.5.6 3.6.1.3 0 .7-.2 1z"/></svg></span>
    +1 555 014 2270
  </div>
  <div class="contact" style="left:283px">
    <span class="ico"><svg width="14" height="14" viewBox="0 0 24 24" fill="#fff"><path d="M6.6 10.8a15 15 0 006.6 6.6l2.2-2.2c.3-.3.7-.4 1-.2 1.1.4 2.3.6 3.6.6.6 0 1 .4 1 1V20c0 .6-.4 1-1 1A17 17 0 013 4c0-.6.4-1 1-1h3.5c.6 0 1 .4 1 1 0 1.3.2 2.5.6 3.6.1.3 0 .7-.2 1z"/></svg></span>
    info@varnothimmigration.com
  </div>
</div>
<a class="abs quote-btn">REQUEST FOR QUOTE</a>
<nav class="abs nav">
  <a>Home</a><span class="sep">|</span><a>About</a><span class="sep">|</span><a>Service &#8964;</a><span class="sep">|</span><a>Testimonials</a><span class="sep">|</span><a>Contact Us</a>
</nav>
<div class="abs lang"><span class="flag"></span><svg width="14" height="10" viewBox="0 0 14 10"><path d="M1 2l6 6 6-6" stroke="#1d2b36" stroke-width="1.6" fill="none"/></svg> Eng</div>

<!-- hero -->
<section class="abs hero" role="img" aria-label="Night view of a steel bridge over the river with the Montreal skyline"></section>
<div class="abs hero-band"></div>
<h1 class="abs" style="left:0;width:1200px;top:218px;text-align:center;color:#fff;font-size:44px;line-height:50px;text-transform:uppercase">Welcome to Varnoth<br>Immigration</h1>
<p class="abs hero-copy">Lorem ipsum dolor sit amet, consectetur adipiscing elit, sed do eiusmod tempor incididunt ut labore et dolore magna aliqua.<br>Ut enim ad minim veniam, quis nostrud exercitation ullamco laboris nisi ut aliquip ex ea commodo consequat.</p>
<a class="abs btn btn-gold" style="left:487px;top:404px;width:225px;height:45px;font-size:16px">Book a Consultation</a>

<!-- about -->
<section class="abs about"></section>
<h2 class="abs" style="left:112px;top:678px;font-size:36px;line-height:43px;color:var(--navy);text-transform:uppercase">About<br>Varnoth Immigration</h2>
<div class="abs about-copy">
  <p><span class="dropcap">L</span>orem ipsum dolor sit amet, consectetur adipiscing elit, sed do eiusmod tempor incididunt ut labore et dolore magna aliqua. Ut enim ad minim veniam, quis nostrud exercitation ullamco laboris nisi ut aliquip ex ea commodo consequat. Duis aute irure dolor in reprehenderit in voluptate velit esse cillum dolore eu fugiat nulla pariatur.</p>
  <p>Ut enim ad minim veniam, quis nostrud exercitation ullamco laboris nisi ut aliquip ex ea commodo consequat. Duis aute irure dolor in reprehenderit in voluptate velit esse cillum dolore eu fugiat nulla pariatur.</p>
</div>
<a class="abs btn btn-navy" style="left:128px;top:1046px;width:138px;height:44px">Read More</a>
<a class="abs btn btn-gold" style="left:274px;top:1046px;width:173px;height:44px">Meet Our Team</a>
<div class="abs frame-a"></div>
<div class="abs frame-b"></div>
<div class="abs photo" style="left:712px;top:689px;width:376px;height:413px" role="img" aria-label="Portrait of the firm's founding attorney"></div>

<!-- practice areas -->
<section class="abs practice"></section>
<h2 class="abs section-title" style="top:1266px;color:#fff">Our Practice Areas Include</h2>

<div class="abs card" style="left:112px;top:1360px;background:linear-gradient(180deg,#7f9a6a,#4e6443)" role="img" aria-label="Family standing together outdoors"><div class="shade"></div><div class="title">Family-Based<br>Immigration</div></div>
<div class="abs card" style="left:361px;top:1360px;background:linear-gradient(180deg,#c5ccd2,#2c3440)" role="img" aria-label="Professional working at a laptop"><div class="shade"></div><div class="title">Employment-Based<br>Immigration</div></div>
<div class="abs card" style="left:611px;top:1360px;background:linear-gradient(180deg,#9db7cf,#6a5a4c)" role="img" aria-label="Group of friends outdoors"><div class="shade"></div><div class="title">Citizenship-Based<br>Immigration</div></div>
<div class="abs card" style="left:861px;top:1360px;background:linear-gradient(180deg,#d6d9de,#3a4a60)" role="img" aria-label="Passport being handed across a desk"><div class="shade"></div><div class="title">Naturalization-Based<br>Immigration</div></div>

<div class="abs card" style="left:112px;top:1667px;background:linear-gradient(180deg,#b8a68c,#5d5247)" role="img" aria-label="Older couple reviewing documents at home"><div class="shade"></div><div class="title">Humanitarian<br>Relief</div></div>
<div class="abs card active" style="left:361px;top:1667px">
  <div class="inner">
    <svg width="72" height="72" viewBox="0 0 72 72"><circle cx="36" cy="36" r="33" fill="none" stroke="#fff" stroke-width="2.5"/><path d="M18 30l18-8 18 8-18 8z" fill="#fff"/><rect x="24" y="38" width="24" height="14" fill="none" stroke="#fff" stroke-width="2.5"/><path d="M54 30v10" stroke="#fff" stroke-width="2"/></svg>
    <h3>Student Visas</h3>
    <p>Lorem ipsum dolor sit amet, consectetur adipiscing elit, sed do incididunt et dolore magna aliqua.</p>
    <svg width="46" height="26" viewBox="0 0 46 26" style="margin-top:8px"><circle cx="33" cy="13" r="11" fill="none" stroke="#fff" stroke-width="1.5"/><path d="M2 13h36M32 8l6 5-6 5" stroke="#fff" stroke-width="1.5" fill="none"/></svg>
  </div>
</div>
<div class="abs card" style="left:611px;top:1667px;background:linear-gradient(180deg,#8a8f94,#2b2f34)" role="img" aria-label="Business investor in a suit"><div class="shade"></div><div class="title">Investor<br>Visas</div></div>
<div class="abs card" style="left:861px;top:1667px;background:linear-gradient(180deg,#c9c287,#2b3645)" role="img" aria-label="Smiling professional in an office"><div class="shade"></div><div class="title">Employment<br>Visas</div></div>

<a class="abs btn outline-btn">View More Practice</a>
<div class="abs practice-band"></div>

<!-- testimonials -->
<h2 class="abs section-title" style="top:2152px;color:var(--navy)">What Our Clients Say?</h2>
<div class="abs testi-card"></div>
<div class="abs testi-band"></div>
<div class="abs quote-box"><svg width="62" height="46" viewBox="0 0 62 46" fill="#fff"><path d="M26 6C14 9 6 17 6 30a10 10 0 1020-2c-1-5-5-8-10-8 2-6 6-9 12-10zM56 6C44 9 36 17 36 30a10 10 0 1020-2c-1-5-5-8-10-8 2-6 6-9 12-10z"/></svg></div>
<p class="abs testi-copy">Lorem ipsum dolor sit amet, consectetur adipiscing elit, sed do eiusmod tempor incididunt ut labore et dolore magna aliqua. Ut enim ad minim veniam, quis nostrud exercitation ullamco laboris nisi ut aliquip ex ea commodo consequat. Duis aute irure dolor in reprehenderit in voluptate velit esse cillum dolore eu fugiat nulla pariatur. Lorem ipsum dolor sit amet, consectetur adipiscing elit, sed do eiusmod tempor incididunt ut labore et dolore magna aliqua. Ut enim ad minim veniam, quis nostrud exercitation ullamco laboris nisi ut aliquip ex ea commodo consequat. Duis aute irure dolor in reprehenderit in voluptate velit esse cillum dolore eu fugiat nulla pariatur.</p>
<p class="abs testi-name">Marc Delorme</p>

<!-- schedule -->
<section class="abs" style="left:0;top:2680px;width:1200px;height:478px;background:#f2f2f2"></section>
<div class="abs skyline" role="img" aria-label="Line illustration of a bridge and city skyline"></div>
<h2 class="abs section-title" style="top:2726px;color:var(--navy)">Schedule a Consultation</h2>
<div class="abs field" style="left:178px;top:2790px;width:413px">First Name *</div>
<div class="abs field" style="left:610px;top:2790px;width:413px">Last Name *</div>
<div class="abs field" style="left:178px;top:2864px;width:413px">Email *</div>
<div class="abs field" style="left:610px;top:2864px;width:413px">Phone</div>
<div class="abs field" style="left:178px;top:2942px;width:845px">Message</div>
<a class="abs btn btn-gold" style="left:530px;top:3030px;width:142px;height:45px">Submit</a>

<!-- footer -->
<footer class="abs footer"></footer>
<div class="abs brand" style="left:452px;top:3222px">
  <span class="mark" style="width:70px;height:70px;background:#3c5463"></span>
  <span class="name" style="font-size:24px;color:#8d9aa3">Varnoth<br>Immigration</span>
</div>
<nav class="abs footer-nav"><a>Home</a><span class="sep">|</span><a>About</a><span class="sep">|</span><a>Service</a><span class="sep">|</span><a>Testimonials</a><span class="sep">|</span><a>Contact Us</a></nav>
<div class="abs divider" style="left:440px"></div>
<div class="abs divider" style="left:776px"></div>
<div class="abs info" style="left:134px">
  <span class="badge"><svg width="20" height="24" viewBox="0 0 20 24"><path d="M10 1a8 8 0 018 8c0 6-8 14-8 14S2 15 2 9a8 8 0 018-8z" fill="#fff"/><circle cx="10" cy="9" r="3" fill="#c4962c"/></svg></span>
  <div><h4>Address:</h4><p>04 , Varnoth ImmigrationLorem<br>ipsum dolor sit 3000</p></div>
</div>
<div class="abs info" style="left:470px">
  <span class="badge"><svg width="20" height="20" viewBox="0 0 24 24" fill="#fff"><path d="M6.6 10.8a15 15 0 006.6 6.6l2.2-2.2c.3-.3.7-.4 1-.2 1.1.4 2.3.6 3.6.6.6 0 1 .4 1 1V20c0 .6-.4 1-1 1A17 17 0 013 4c0-.6.4-1 1-1h3.5c.6 0 1 .4 1 1 0 1.3.2 2.5.6 3.6.1.3 0 .7-.2 1z"/></svg></span>
  <div><h4>Phone Number:</h4><p>+1 555 014 2270</p></div>
</div>
<div class="abs info" style="left:812px">
  <span class="badge"><svg width="22" height="16" viewBox="0 0 22 16"><rect x="1" y="1" width="20" height="14" fill="#fff"/><path d="M1 1l10 8 10-8" stroke="#c4962c" stroke-width="1.6" fill="none"/></svg></span>
  <div><h4>Email Address</h4><p>Info@varnothimmigration.in</p></div>
</div>
<div class="abs legal">© 2023 Varnoth Immigration | All Rights Reserved</div>

</body>
</html>
```